Business card for a shipping supplies business

Needing a business card design. Please see the logo. The logo with the white font should be used if there is a dark background.

We are looking for the following info on the card. Please see the sample info. We will need the info to be changed with a few different employee names and info but all will use the same template.

Business Name: The Crate Heron
Employee Name : Marcus Delaney
Position: Account Manager
Address: 4827 W. Ridge 418 S.
Larkmoor, OK 73948
email: Marcus@thecrateheron.example
telephone: 855-619-2740 x 207
website: www.getparcelkits.example

Target Market(s)

Businesses who ship products for online sales

Industry/Entity Type

Cardboard

Contact Information for Business Card

Name, title, address, website, logo, telephone number

Font styles to use
Sans Serif

Colors
EE7325
F08F49
F5BC92
FAE3D3
FDF4ED

Requirements
Must have
• Logo on back of card. Clean look, just logo, website address

```html
<!DOCTYPE html>
<html lang="en">
<head>
<meta charset="utf-8">
<title>The Crate Heron – Business Card</title>
<link href="https://fonts.googleapis.com/css2?family=Montserrat:wght@400;500;600;700&display=swap" rel="stylesheet">
<style>
  :root {
    --bg: #e4e4e4;
    --ink: #161616;
    --paper: #ffffff;
    --orange: #ee7325;
    --orange-mid: #f08f49;
    --orange-deep: #c4511a;
    --rust: #7a2a10;
    --text-dark: #2a2a2a;
    --white: #ffffff;
  }
  * { box-sizing: border-box; margin: 0; padding: 0; }
  html, body {
    width: 1200px; height: 800px; overflow: hidden;
    background: var(--bg);
    font-family: "Montserrat", sans-serif;
  }
  .canvas {
    position: relative; width: 1200px; height: 800px;
  }
  .card {
    position: absolute;
    width: 540px; height: 309px;
    border-radius: 20px;
    overflow: hidden;
    box-shadow: 0 14px 30px rgba(0,0,0,0.22);
  }
  .card--front { left: 40px; top: 246px; background: var(--paper); }
  .card--back  { left: 620px; top: 246px; background: var(--ink); }

  .front-shape { position: absolute; inset: 0; }

  .name-band {
    position: absolute; left: 0; top: 72px;
    width: 262px; height: 62px;
    background: linear-gradient(90deg, var(--orange) 0%, var(--orange-deep) 55%, var(--rust) 100%);
    padding: 9px 0 0 38px;
    color: var(--white);
  }
  .name-band__name {
    font-weight: 700; font-size: 20px; letter-spacing: 0.5px; line-height: 1.15;
  }
  .name-band__title {
    font-weight: 400; font-size: 13px; line-height: 1.3;
  }

  .contact-list {
    position: absolute; left: 38px; top: 156px;
    list-style: none;
    color: var(--text-dark);
    font-size: 11.5px; line-height: 1.45;
  }
  .contact-list__item {
    display: flex; align-items: flex-start; gap: 8px;
    margin-bottom: 3px;
  }
  .contact-icon {
    flex: none; width: 16px; height: 16px; margin-top: 1px;
  }

  .brand-name {
    position: absolute;
    color: var(--white);
    font-weight: 700;
    text-align: center;
    white-space: nowrap;
  }
  .card--front .brand-name {
    right: 34px; top: 86px; width: 190px;
    font-size: 22px; line-height: 1.2; white-space: normal;
  }
  .brand-dot {
    display: block; margin: 0 auto 12px;
    width: 34px; height: 34px; border-radius: 50%;
    background: var(--orange);
  }
  .card--back .brand-name {
    left: 0; right: 0; top: 96px;
    font-size: 36px;
  }
  .back-site {
    position: absolute; left: 0; right: 0; top: 196px;
    display: flex; justify-content: center; align-items: center; gap: 8px;
    color: var(--white); font-size: 15px; font-weight: 500;
  }
</style>
</head>
<body>
<main class="canvas">

  <section class="card card--front" aria-label="Card front">
    <svg class="front-shape" width="540" height="309" viewBox="0 0 540 309">
      <path d="M284 0 C242 112 282 244 420 309 L540 309 L540 0 Z" fill="var(--orange)"/>
      <path d="M296 0 C256 110 294 238 432 309 L540 309 L540 0 Z" fill="var(--ink)"/>
    </svg>

    <div class="name-band">
      <p class="name-band__name">MARCUS DELANEY</p>
      <p class="name-band__title">Account Manager</p>
    </div>

    <ul class="contact-list">
      <li class="contact-list__item">
        <svg class="contact-icon" viewBox="0 0 16 16" aria-hidden="true"><circle cx="8" cy="8" r="8" fill="var(--orange)"/><path d="M8 3.5a2.8 2.8 0 0 0-2.8 2.8C5.2 8.5 8 12 8 12s2.8-3.5 2.8-5.7A2.8 2.8 0 0 0 8 3.5z" fill="#fff"/><circle cx="8" cy="6.3" r="1" fill="var(--orange)"/></svg>
        <span>4827 W. Ridge 418 S.<br>Larkmoor, OK 73948</span>
      </li>
      <li class="contact-list__item">
        <svg class="contact-icon" viewBox="0 0 16 16" aria-hidden="true"><circle cx="8" cy="8" r="8" fill="var(--orange)"/><path d="M5.6 4.2l1.3 1.8-.8 1c.5 1 1.3 1.8 2.3 2.3l1-.8 1.8 1.3-.7 1.5C7.6 11.2 4.8 8.4 4.7 5l.9-.8z" fill="#fff"/></svg>
        <span>855-619-2740 x 207</span>
      </li>
      <li class="contact-list__item">
        <svg class="contact-icon" viewBox="0 0 16 16" aria-hidden="true"><circle cx="8" cy="8" r="8" fill="var(--orange)"/><rect x="4" y="5.2" width="8" height="5.6" rx="0.6" fill="#fff"/><path d="M4.2 5.5L8 8.4l3.8-2.9" stroke="var(--orange)" stroke-width="0.9" fill="none"/></svg>
        <span>Marcus@thecrateheron.example</span>
      </li>
      <li class="contact-list__item">
        <svg class="contact-icon" viewBox="0 0 16 16" aria-hidden="true"><circle cx="8" cy="8" r="8" fill="var(--orange)"/><circle cx="8" cy="8" r="4" fill="none" stroke="#fff" stroke-width="1"/><path d="M4 8h8M8 4c-1.6 2.4-1.6 5.6 0 8M8 4c1.6 2.4 1.6 5.6 0 8" stroke="#fff" stroke-width="0.8" fill="none"/></svg>
        <span>www.getparcelkits.example</span>
      </li>
    </ul>

    <p class="brand-name"><span class="brand-dot"></span>The Crate Heron</p>
  </section>

  <section class="card card--back" aria-label="Card back">
    <p class="brand-name">The Crate Heron</p>
    <p class="back-site">
      <svg class="contact-icon" viewBox="0 0 16 16" aria-hidden="true"><circle cx="8" cy="8" r="8" fill="var(--orange)"/><circle cx="8" cy="8" r="4" fill="none" stroke="#fff" stroke-width="1"/><path d="M4 8h8M8 4c-1.6 2.4-1.6 5.6 0 8M8 4c1.6 2.4 1.6 5.6 0 8" stroke="#fff" stroke-width="0.8" fill="none"/></svg>
      <span>getparcelkits.example</span>
    </p>
  </section>

</main>
</body>
</html>
```